Tarrow Building Performance

Id like for my business card to be very bold and professional. Incorporating the business logo, the main services offered, and my contact info. Services are spray foam, insulation, new construction, retrofit, weatherization.

When opening this project sketch harbor was not able to upload my new logo that I picked from another recent sketch harbor project. Does anyone know how i could upload my logo onto the page for design of the business cards?

Target Market(s)

Building owners, contractors

Industry/Entity Type

Building Insulation and performance improvements

Contact Information for Business Card

Owner, Email dean@tarrowbuildingperformance.example Phone number 555-208-6147

Colors
0054AA
0677BA
7BADD7
CADEEF
E8F1F8
F0912C
F2A743
F7CA91
FBE8D2
FDF5EE

Requirements
Must have
• Services- spray foam, cellulose, mineral wool, fiberglass, air sealing, new construction, retrofit, weatherization, energy saving assesments

```html
<!DOCTYPE html>
<html lang="en">
<head>
<meta charset="UTF-8">
<title>Tarrow Building Performance – Business Card</title>
<link href="https://fonts.googleapis.com/css2?family=Poppins:wght@400;500;600;800&display=swap" rel="stylesheet">
<style>
  :root {
    --stage: #2b2c2f;
    --navy: #0b1536;
    --orange: #ec7622;
    --sky: #39aee6;
    --white: #ffffff;
    --silver: #c9ccd3;
    --rule: #6b7390;
  }
  * { box-sizing: border-box; margin: 0; padding: 0; }
  html, body {
    width: 1200px; height: 952px; overflow: hidden;
    background: var(--stage);
    font-family: "Poppins", sans-serif;
  }
  .card {
    position: absolute; left: 250px; width: 700px; height: 400px;
    background: var(--navy); overflow: hidden;
    box-shadow: 0 10px 30px rgba(0,0,0,.45);
  }
  .card--contact { top: 50px; }
  .card--services { top: 502px; }

  /* contact side */
  .person { position: absolute; left: 70px; top: 70px; }
  .person__name { font-size: 30px; letter-spacing: 1px; line-height: 1.1; }
  .person__first { color: var(--sky); font-weight: 500; }
  .person__last { color: var(--orange); font-weight: 800; }
  .person__role { color: var(--white); font-size: 17px; margin-top: 4px; }
  .person__rule { width: 46px; height: 2px; background: var(--rule); margin: 10px 0 16px; }
  .contact-line { display: flex; align-items: center; gap: 12px; color: var(--white); font-size: 15px; margin-bottom: 12px; }
  .contact-line__icon { width: 24px; height: 24px; background: var(--orange); border-radius: 3px; display: flex; align-items: center; justify-content: center; flex: none; }

  /* company name */
  .company {
    position: absolute; display: flex; align-items: center; gap: 10px;
    color: var(--white); font-weight: 600; font-size: 18px; white-space: nowrap;
  }
  .company__dot { width: 10px; height: 10px; border-radius: 50%; background: var(--white); flex: none; }
  .company--footer { right: 50px; bottom: 46px; }
  .company--header { left: 0; right: 0; top: 60px; justify-content: center; font-size: 22px; }

  /* services side */
  .services-band {
    position: absolute; left: 0; right: 0; top: 150px; height: 160px;
    background: var(--orange);
    border-top: 3px solid var(--silver); border-bottom: 3px solid var(--silver);
    display: grid; grid-template-columns: 1.25fr 1fr 1.3fr; padding: 22px 36px;
  }
  .service-list { list-style: none; }
  .service-list li { display: flex; align-items: center; gap: 8px; color: var(--white); font-size: 15px; font-weight: 500; margin-bottom: 10px; white-space: nowrap; }
  .tick { width: 15px; height: 15px; background: var(--navy); display: flex; align-items: center; justify-content: center; flex: none; }
</style>
</head>
<body>

<section class="card card--contact">
  <div class="person">
    <h1 class="person__name"><span class="person__first">MARTIN J. </span><span class="person__last">CALLOWAY</span></h1>
    <p class="person__role">Owner</p>
    <div class="person__rule"></div>
    <p class="contact-line">
      <span class="contact-line__icon">
        <svg width="14" height="14" viewBox="0 0 24 24"><path fill="#fff" d="M6.6 10.8a15.1 15.1 0 0 0 6.6 6.6l2.2-2.2c.3-.3.7-.4 1-.2 1.1.4 2.3.6 3.6.6.6 0 1 .4 1 1V20c0 .6-.4 1-1 1A17 17 0 0 1 3 4c0-.6.4-1 1-1h3.5c.6 0 1 .4 1 1 0 1.3.2 2.5.6 3.6.1.3 0 .7-.2 1z"/></svg>
      </span>
      +555-208-6147
    </p>
    <p class="contact-line">
      <span class="contact-line__icon">
        <svg width="14" height="12" viewBox="0 0 24 18"><rect x="1" y="1" width="22" height="16" fill="none" stroke="#fff" stroke-width="2"/><path d="M1 1l11 9 11-9" fill="none" stroke="#fff" stroke-width="2"/></svg>
      </span>
      dean@tarrowbuildingperformance.example
    </p>
  </div>
  <p class="company company--footer"><span class="company__dot"></span>Tarrow Building Performance</p>
</section>

<section class="card card--services">
  <p class="company company--header"><span class="company__dot"></span>Tarrow Building Performance</p>
  <div class="services-band">
    <ul class="service-list">
      <li><span class="tick"><svg width="11" height="11" viewBox="0 0 12 12"><path d="M2 6l3 3 5-6" fill="none" stroke="#fff" stroke-width="2"/></svg></span>Services- Spray Foam</li>
      <li><span class="tick"><svg width="11" height="11" viewBox="0 0 12 12"><path d="M2 6l3 3 5-6" fill="none" stroke="#fff" stroke-width="2"/></svg></span>Cellulose</li>
      <li><span class="tick"><svg width="11" height="11" viewBox="0 0 12 12"><path d="M2 6l3 3 5-6" fill="none" stroke="#fff" stroke-width="2"/></svg></span>Mineral Wool</li>
    </ul>
    <ul class="service-list">
      <li><span class="tick"><svg width="11" height="11" viewBox="0 0 12 12"><path d="M2 6l3 3 5-6" fill="none" stroke="#fff" stroke-width="2"/></svg></span>Fiberglass</li>
      <li><span class="tick"><svg width="11" height="11" viewBox="0 0 12 12"><path d="M2 6l3 3 5-6" fill="none" stroke="#fff" stroke-width="2"/></svg></span>Air Sealing</li>
      <li><span class="tick"><svg width="11" height="11" viewBox="0 0 12 12"><path d="M2 6l3 3 5-6" fill="none" stroke="#fff" stroke-width="2"/></svg></span>New Construction</li>
    </ul>
    <ul class="service-list">
      <li><span class="tick"><svg width="11" height="11" viewBox="0 0 12 12"><path d="M2 6l3 3 5-6" fill="none" stroke="#fff" stroke-width="2"/></svg></span>Retrofit</li>
      <li><span class="tick"><svg width="11" height="11" viewBox="0 0 12 12"><path d="M2 6l3 3 5-6" fill="none" stroke="#fff" stroke-width="2"/></svg></span>Weatherization</li>
      <li><span class="tick"><svg width="11" height="11" viewBox="0 0 12 12"><path d="M2 6l3 3 5-6" fill="none" stroke="#fff" stroke-width="2"/></svg></span>Energy Saving Assesments</li>
    </ul>
  </div>
</section>

</body>
</html>
```